Co-Living Retreat Centre Pitch Deck

We are needing fresh new pitch deck for our Co-Living Retreat Centre project. We are building a 40 unit community focused on personal development and holistic living!

Here is the branding guide:
https://www.plorvex.com/sheet/QWRT8mHkzp3/vbLoPnXaTd_4uR-7eWsMqY/open

Here is the Content:
https://files.tamberlo.com/store/boxes/8K4Pm2vRtXw7nQ91bLzHyE5cJd3sFa0Gq?mode=viewing

Target Market(s)

30-45 Year olds that are into Yoga, Meditation, Personal Development, Balance Lifestyle.

Font styles to use
Serif
Sans Serif

Requirements
Must have
• Must have the colours from our branding.
Nice to have
• Have some elements of nature, Inspiration,

```html
<!DOCTYPE html>
<html lang="en">
<head>
<meta charset="utf-8">
<title>Kalindra – Co-Living Retreat Pitch Deck</title>
<link rel="stylesheet" href="https://fonts.googleapis.com/css2?family=Inter:wght@400;600;700;800&family=Cormorant+Garamond:wght@500;600&display=swap">
<style>
:root{
  --gold:#C29F33;
  --white:#FFFFFF;
  --grey-band:#ECECEC;
  --ink:#2B2B2B;
  --logo-grey:#7E7E7E;
  --sage:#6B8A69;
  --leaf:#3F7A2A;
  --muted:#6A6A6A;
}
*{margin:0;padding:0;box-sizing:border-box}
html,body{width:1200px;height:3708px;overflow:hidden;background:#fff}
body{position:relative;font-family:'Inter',Arial,sans-serif}
.slide{position:absolute;left:164px;width:881px;height:497px;background:var(--white);overflow:hidden;box-shadow:0 1px 4px rgba(0,0,0,.25)}
.band{position:absolute;left:0;top:0;width:100%;background:var(--gold)}
.footer{position:absolute;left:0;bottom:0;width:100%;height:35px;background:var(--grey-band);font-size:6px;color:var(--muted);text-align:center;line-height:35px}
.wordmark{position:absolute;font-weight:700;font-size:40px;letter-spacing:.5px;color:var(--logo-grey);line-height:1}
.leaf{position:absolute;right:0;width:200px;height:150px;background:radial-gradient(ellipse at 80% 50%,rgba(63,122,42,.85),rgba(63,122,42,.35) 55%,rgba(63,122,42,0) 75%)}
.serif-title{position:absolute;left:0;width:100%;text-align:center;font-family:'Cormorant Garamond',Georgia,serif;font-weight:500;font-size:56px;color:var(--white);line-height:1}
.photo{position:absolute}
.serif-head{position:absolute;font-family:'Cormorant Garamond',Georgia,serif;font-weight:500;font-size:32px;line-height:1}
.body-copy{position:absolute;font-size:9.5px;line-height:17px}
.small-copy{font-size:8px;line-height:12.5px;color:var(--white)}

/* cover */
.cover-title{position:absolute;left:46px;top:120px;font-weight:800;font-size:52px;color:var(--white);line-height:1}
.cover-sub{position:absolute;left:46px;top:186px;font-size:20px;color:var(--white)}

/* targeting */
.audience{position:absolute;top:168px;width:142px}
.audience .photo{position:static;width:142px;height:178px}
.audience-label{margin-top:10px;font-weight:700;font-size:13px;color:var(--ink);line-height:15px}

/* facilities */
.facility{position:absolute;width:91px;height:328px}
.facility-label{position:absolute;left:0;top:40px;width:100%;display:flex;justify-content:center;writing-mode:vertical-rl;font-weight:700;font-size:20px;color:var(--white);letter-spacing:.5px;white-space:nowrap}
</style>
</head>
<body>

<!-- Cover -->
<section class="slide" style="top:128px">
  <div class="band" style="height:339px"></div>
  <div class="leaf" role="img" aria-label="Palm frond" style="top:170px"></div>
  <h1 class="cover-title">The Kalindra</h1>
  <p class="cover-sub">The greatest quest in life is to reach one’s highest potential.</p>
  <div class="wordmark" style="right:48px;top:381px;color:var(--ink)">Kalindra</div>
  <div class="footer">© 2021. The Company name . All Rights Reserved</div>
</section>

<!-- Vision & Mission -->
<section class="slide" style="top:724px">
  <div class="band" style="height:211px"></div>
  <div class="leaf" role="img" aria-label="Palm frond" style="top:40px"></div>
  <h2 class="serif-title" style="top:26px">Vision &amp; Mission</h2>
  <div class="photo" role="img" aria-label="Woman meditating in sunlit forest" style="left:107px;top:108px;width:319px;height:203px;background:linear-gradient(160deg,#d9d2bf,#4a4a3a 55%,#1f2418)"></div>
  <div class="photo" role="img" aria-label="Group yoga class in open pavilion" style="left:455px;top:108px;width:319px;height:203px;background:linear-gradient(180deg,#3b3a34,#8b9a88 45%,#b8c2c6)"></div>
  <h3 class="serif-head" style="left:107px;top:318px;color:var(--ink)">Mission</h3>
  <p class="body-copy" style="left:107px;top:352px;width:319px;font-size:9px;color:var(--muted)">To shape conscious co-living spaces and experiences where facilitators, creatives, entrepreneurs and wanderers alike come together to reach their highest potential. Creating a sanctuary for those who crave growth, connection and self-actualization.</p>
  <h3 class="serif-head" style="left:455px;top:318px;color:var(--ink)">Vision</h3>
  <p class="body-copy" style="left:455px;top:352px;width:319px;font-size:9px;color:var(--muted)">Creating communities and experiences that revolutionize optimal living and evoke transformation. Empowering co-creation passion and purpose to awaken the ultimate self.</p>
  <div class="wordmark" style="right:9px;top:417px">Kalindra</div>
  <div class="footer">© 2021. The Company name . All Rights Reserved</div>
</section>

<!-- Problem & Promise -->
<section class="slide" style="top:1320px">
  <div class="band" style="height:407px"></div>
  <div class="leaf" role="img" aria-label="Palm frond" style="top:230px"></div>
  <h2 class="serif-head" style="left:43px;top:35px;color:var(--white)">The Problem</h2>
  <div class="body-copy small-copy" style="left:43px;top:82px;width:290px">
    <p>Majority of our western civilization has become disconnected from themselves, nature and others. Chasing material possessions in a concrete jungle. Loneliness and stress has become an epidemic.</p>
    <p style="margin-top:12px">People are seeking a place to live and grow in a community of like minded people that inspire and support their growth and passions.</p>
  </div>
  <h2 class="serif-head" style="left:370px;top:35px;color:var(--white)">Our Promise</h2>
  <p class="body-copy small-copy" style="left:370px;top:82px;width:300px;text-align:justify">Our purpose is to create a transformative hub for change makers seeking personal development and optimal living with a desire to always drive positive change in the world. We inspire people to live a balanced lifestyle that fosters a deeper connection to themselves, others and nature. Creating an optimised way of life that covers all areas of success, health and wealth.</p>
  <div class="photo" role="img" aria-label="Sound bath session with singing bowls" style="left:43px;top:181px;width:303px;height:194px;background:linear-gradient(170deg,#3a4148,#6b5a44 55%,#2c2a26)"></div>
  <div class="photo" role="img" aria-label="Outdoor massage on treatment table in garden" style="left:370px;top:181px;width:303px;height:194px;background:linear-gradient(180deg,#2f4a22,#5f7d3c 55%,#8a9b6c)"></div>
  <div class="wordmark" style="right:9px;top:415px">Kalindra</div>
  <div class="footer">© 2021. The Company name . All Rights Reserved</div>
</section>

<!-- Targeting -->
<section class="slide" style="top:1916px">
  <div class="band" style="height:258px"></div>
  <div class="leaf" role="img" aria-label="Palm frond" style="top:150px"></div>
  <h2 class="serif-title" style="top:27px">Who are we targeting?</h2>
  <p style="position:absolute;left:0;top:92px;width:100%;text-align:center;font-size:20px;color:var(--white)">We are seeking those who envision more depth, meaning and purpose in their lives.</p>
  <p style="position:absolute;left:0;top:120px;width:100%;text-align:center;font-family:'Cormorant Garamond',Georgia,serif;font-weight:500;font-size:19px;color:var(--white)">A collaboration of creative people that together, fuel unforgettable and life-changing experiences.</p>
  <div class="audience" style="left:13px"><div class="photo" role="img" aria-label="Yoga facilitator in tree pose" style="background:linear-gradient(180deg,#cfd6d0,#8f9a8c)"></div><p class="audience-label">Facilitators</p></div>
  <div class="audience" style="left:155px"><div class="photo" role="img" aria-label="Group walking down steps" style="background:linear-gradient(180deg,#9aa09a,#d8d5cf)"></div><p class="audience-label">Entrepreneurs</p></div>
  <div class="audience" style="left:298px"><div class="photo" role="img" aria-label="Yoga practice in studio" style="background:linear-gradient(180deg,#6f6558,#c2b8a6)"></div><p class="audience-label">Experience<br>Creators</p></div>
  <div class="audience" style="left:440px"><div class="photo" role="img" aria-label="Woman working on laptop" style="background:linear-gradient(180deg,#9a8e7c,#3d5a5c)"></div><p class="audience-label">Social Impact<br>Investors</p></div>
  <div class="audience" style="left:583px"><div class="photo" role="img" aria-label="Man at laptop with headphones" style="background:linear-gradient(180deg,#a7b7a0,#d6d9d2)"></div><p class="audience-label">Remote Workers</p></div>
  <div class="audience" style="left:725px"><div class="photo" role="img" aria-label="Poolside lounging under red umbrella" style="background:linear-gradient(180deg,#b5524a,#6fb8c4 55%,#2f8fa0)"></div><p class="audience-label">Artists</p></div>
  <div class="wordmark" style="right:9px;top:415px">Kalindra</div>
  <div class="footer">© 2021. The Company name . All Rights Reserved</div>
</section>

<!-- Location -->
<section class="slide" style="top:2511px">
  <div class="band" style="height:271px"></div>
  <div class="leaf" role="img" aria-label="Palm frond" style="top:110px"></div>
  <h2 class="serif-title" style="top:27px">Our Location</h2>
  <div style="position:absolute;left:97px;top:110px;width:348px;height:288px;background:var(--sage)"></div>
  <h3 class="serif-head" style="left:118px;top:160px;color:var(--white)">The Property</h3>
  <p class="body-copy" style="left:118px;top:209px;width:305px;line-height:20.5px;color:var(--white);text-align:justify">Nestled in the lush jungle of Bali between Canggu and Ubud, our incredible property sits on 2.2 hectares of land with a large river that flows through. We host 10 rooms at present and soon to be 30 more, expanding our scenic space so we can co-create new ideas, projects and technology that enable a healthier lifestyle.</p>
  <div class="photo" role="img" aria-label="Evening lounge with red pendant lamp and sofas" style="left:445px;top:110px;width:340px;height:288px;background:linear-gradient(180deg,#3a2a22,#7a2a22 30%,#4a3a32 60%,#8a7a70)"></div>
  <div class="wordmark" style="right:9px;top:415px">Kalindra</div>
  <div class="footer">© 2021. The Company name . All Rights Reserved</div>
</section>

<!-- Facilities -->
<section class="slide" style="top:3107px">
  <div class="band" style="height:255px"></div>
  <div class="leaf" role="img" aria-label="Palm frond" style="top:110px"></div>
  <h2 class="serif-title" style="top:10px">Facilities</h2>
  <div class="facility" role="img" aria-label="Yoga shala" style="left:30px;top:84px;background:linear-gradient(180deg,#3c4a32,#7a6a58)"><span class="facility-label">2 YOGA SHALAS</span></div>
  <div class="facility" role="img" aria-label="Co-working space" style="left:122px;top:71px;background:linear-gradient(180deg,#5a4a40,#8a7060)"><span class="facility-label">CO-WORKING SPACE</span></div>
  <div class="facility" role="img" aria-label="Gym" style="left:213px;top:104px;background:linear-gradient(180deg,#6a5a4c,#b49a84)"><span class="facility-label" style="top:120px">GYM</span></div>
  <div class="facility" role="img" aria-label="Sauna" style="left:304px;top:71px;background:linear-gradient(180deg,#4a5a3a,#7a4a6a)"><span class="facility-label" style="top:120px">SAUNA</span></div>
  <div class="facility" role="img" aria-label="Cold plunge pool" style="left:396px;top:93px;background:linear-gradient(180deg,#3a5a42,#2a9aa0)"><span class="facility-label" style="top:80px">COLD PLUNGE</span></div>
  <div class="facility" role="img" aria-label="Hot tub" style="left:487px;top:71px;background:linear-gradient(180deg,#8a7a70,#b8aaa0)"><span class="facility-label" style="top:120px">HOT TUB</span></div>
  <div class="facility" role="img" aria-label="Workshop space" style="left:578px;top:93px;background:linear-gradient(180deg,#3a3a38,#6a6a60)"><span class="facility-label">WORKSHOP SPACES</span></div>
  <div class="facility" role="img" aria-label="Healing pods" style="left:670px;top:65px;background:linear-gradient(180deg,#6a7a5a,#9a8a7a)"><span class="facility-label" style="top:60px">HEALING PODS</span></div>
  <div class="facility" role="img" aria-label="Amphitheater" style="left:761px;top:84px;background:linear-gradient(180deg,#5a4a44,#c8bcb0)"><span class="facility-label">AMPHITHEATER</span></div>
  <div class="wordmark" style="right:9px;top:415px">Kalindra</div>
  <div class="footer">© 2021. The Company name . All Rights Reserved</div>
</section>

</body>
</html>
```